Qorvane VoIP COMMERCIAL PHONE FLYER

We are a full service telecom VoIP company that offers local, long distance calling plans to business clients. We offer local installations, and local service we have a hands on approach and will match or beat any competitor. We work with all types of business. We are fully HIPPA complient in the medical field

Target Market(s)

SMALL TO MEDIUM BUSINESS, Medical, Real Estate, Lawyer, Accounting

Industry/Entity Type

VoIP

Font styles to use
Serif

Colors
0054AA
0677BA
7BADD7
CADEEF
E8F1F8

Requirements
Must have
• Modern/ Current picture of phone reader friendly
Nice to have
• free flow, friendly, modern
Should not have
• stuffy, corporate feel

```html
<!DOCTYPE html>
<html lang="en">
<head>
<meta charset="utf-8">
<title>Qorvane VoIP – Your Business on the Cloud</title>
<link href="https://fonts.googleapis.com/css2?family=Montserrat:ital,wght@0,400;0,600;0,800;0,900;1,300;1,400;1,800;1,900&family=Rajdhani:wght@500;600;700&display=swap" rel="stylesheet">
<style>
  :root{
    --navy-deep:#0b1838;
    --navy:#14285a;
    --blue-brand:#0054AA;
    --blue-mid:#0677BA;
    --blue-soft:#7BADD7;
    --blue-pale:#CADEEF;
    --blue-mist:#E8F1F8;
    --cyan:#2fa8ff;
    --yellow:#fff200;
    --graphite:#2a2d33;
    --white:#ffffff;
  }
  *{margin:0;padding:0;box-sizing:border-box}
  html,body{width:848px;height:1200px;overflow:hidden;background:var(--navy-deep)}
  .flyer{
    position:relative;width:848px;height:1200px;overflow:hidden;
    font-family:"Montserrat",sans-serif;color:var(--white);
    background:
      radial-gradient(ellipse 380px 320px at 420px 430px, rgba(123,173,215,.9) 0%, rgba(6,119,186,.55) 40%, rgba(0,84,170,0) 78%),
      linear-gradient(180deg,#0a5fb8 0%,#0b4f9d 35%,#123a7a 60%,#14285a 75%,#172a5e 100%);
  }

  .office-icons{position:absolute;left:160px;top:0;width:340px;height:480px;
    background:radial-gradient(ellipse at 60% 45%, rgba(202,222,239,.35), rgba(123,173,215,.12) 55%, rgba(0,84,170,0) 80%)}
  .network-globe{position:absolute;left:468px;top:100px;width:346px;height:368px;border-radius:50%;
    background:radial-gradient(circle at 40% 55%, var(--blue-mist) 0%, var(--blue-pale) 30%, var(--blue-soft) 58%, rgba(6,119,186,.55) 100%);
    box-shadow:0 0 40px rgba(202,222,239,.45)}
  .desk-phone{position:absolute;left:268px;top:212px;width:382px;height:258px;border-radius:22px 22px 26px 40px;
    background:linear-gradient(160deg,#4a4f57 0%,var(--graphite) 45%,#111317 100%);
    box-shadow:0 18px 30px rgba(0,0,0,.45)}

  .brand-top{position:absolute;left:648px;top:42px;font-family:"Rajdhani",sans-serif;font-weight:700;
    font-size:46px;letter-spacing:2px;color:var(--cyan)}

  .headline{position:absolute;left:0;width:848px;text-align:center;font-weight:900;font-style:italic;
    text-shadow:0 0 18px rgba(47,168,255,.55),0 2px 0 var(--blue-brand)}
  .headline--business{top:522px;font-size:64px;letter-spacing:-1px;left:-8px}
  .headline--cloud{top:588px;left:-3px}
  .headline--cloud .small{font-size:44px;letter-spacing:-1px}
  .headline--cloud .big{font-size:84px;letter-spacing:-2px}

  .savings{position:absolute;left:143px;top:730px;font-style:italic}
  .savings__intro{font-weight:800;font-size:28px;letter-spacing:4px}
  .savings__amount{font-weight:900;font-size:56px;letter-spacing:4px;color:var(--yellow);line-height:1;margin-top:2px}
  .savings__tail{font-weight:400;font-size:30px;letter-spacing:4px;line-height:1.05}
  .savings__tail--small{font-size:24px;letter-spacing:3px}
  .badge{position:absolute;left:562px;top:728px;width:140px;height:140px;border-radius:50%;
    background:radial-gradient(circle at 40% 30%,#ff6a6a 0%,#e81d1f 40%,#a80608 100%);
    box-shadow:0 6px 18px rgba(0,0,0,.45);display:flex;align-items:center;justify-content:center;
    font-weight:900;font-style:italic;font-size:56px;letter-spacing:-1px}

  .feature-band{position:absolute;left:0;top:902px;width:848px;height:149px;background:var(--navy-deep)}
  .checklist{position:absolute;left:65px;top:16px;list-style:none}
  .checklist li{display:flex;align-items:center;gap:6px;height:17.2px;font-weight:800;font-style:italic;
    font-size:13.5px;letter-spacing:1.6px}
  .checklist svg{flex:none}
  .feature{position:absolute;top:20px;width:130px;text-align:center;font-family:"Rajdhani",sans-serif;
    font-weight:500;font-size:13px;letter-spacing:1.8px;line-height:1.1}
  .feature__icon{width:70px;height:70px;border-radius:50%;margin:0 auto 18px;
    background:radial-gradient(circle at 50% 35%,#2a8fd6,#0a4f9a);display:flex;align-items:center;justify-content:center}
  .feature--features{left:382px}.feature--ease{left:548px}.feature--setup{left:695px}

  .footer{position:absolute;left:0;top:1051px;width:848px;height:149px;background:var(--navy)}
  .brand-bottom{position:absolute;left:50px;top:54px;font-family:"Rajdhani",sans-serif;font-weight:700;
    font-size:48px;letter-spacing:2px;color:var(--cyan)}
  .cta{position:absolute;left:200px;width:448px;top:36px;text-align:center;font-style:italic;font-size:14px;letter-spacing:1.8px;font-weight:300}
  .cta b{font-weight:900}
  .phone-pill{position:absolute;left:265px;top:61px;width:318px;height:37px;border-radius:19px;
    background:linear-gradient(180deg,#2d8fe0,#0a5fae);display:flex;align-items:center;justify-content:center;gap:12px;
    font-family:"Rajdhani",sans-serif;font-weight:700;font-size:32px;letter-spacing:5px}
  .web{position:absolute;left:640px;width:156px;top:37px;text-align:center;font-family:"Rajdhani",sans-serif;font-weight:600;font-size:13px;letter-spacing:1.3px}
  .socials{position:absolute;left:650px;top:58px;width:138px;display:flex;flex-wrap:wrap;justify-content:center;gap:6px 8px;list-style:none}
  .socials li{font-family:"Rajdhani",sans-serif;font-weight:600;font-size:11px;letter-spacing:.5px;
    padding:3px 7px;border-radius:10px;background:var(--blue-mid);color:var(--white)}
</style>
</head>
<body>
<main class="flyer">
  <div class="office-icons" role="img" aria-label="Floating office icons: documents, mail, chat bubbles, people and growth charts"></div>
  <div class="network-globe" role="img" aria-label="Glowing globe wrapped in a network of connected lines"></div>
  <div class="desk-phone" role="img" aria-label="Modern HD desk video phone with coiled handset and touchscreen showing a video call"></div>
  <div class="brand-top">Qorvane</div>

  <h1>
    <span class="headline headline--business">YOUR BUSINESS</span>
    <span class="headline headline--cloud"><span class="small">ON THE </span><span class="big">CLOUD</span></span>
  </h1>

  <section class="savings">
    <p class="savings__intro">WE HELP COMPANIES</p>
    <p class="savings__amount">SAVE OVER</p>
    <p class="savings__tail">ON THEIR MONTHLY</p>
    <p class="savings__tail savings__tail--small">PHONE BILLS</p>
  </section>
  <div class="badge">35%</div>

  <section class="feature-band">
    <ul class="checklist">
      <li><svg width="13" height="13" viewBox="0 0 13 13"><circle cx="6.5" cy="6.5" r="6.5" fill="#fff200"/><path d="M3.6 6.7l2 2 3.8-4" stroke="#0b1838" stroke-width="1.6" fill="none"/></svg>KEEP YOUR TELEPHONE NUMBERS.</li>
      <li><svg width="13" height="13" viewBox="0 0 13 13"><circle cx="6.5" cy="6.5" r="6.5" fill="#fff200"/><path d="M3.6 6.7l2 2 3.8-4" stroke="#0b1838" stroke-width="1.6" fill="none"/></svg>NO LONG TERM CONTRACTS.</li>
      <li><svg width="13" height="13" viewBox="0 0 13 13"><circle cx="6.5" cy="6.5" r="6.5" fill="#fff200"/><path d="M3.6 6.7l2 2 3.8-4" stroke="#0b1838" stroke-width="1.6" fill="none"/></svg>MONTH TO MONTH.</li>
      <li><svg width="13" height="13" viewBox="0 0 13 13"><circle cx="6.5" cy="6.5" r="6.5" fill="#fff200"/><path d="M3.6 6.7l2 2 3.8-4" stroke="#0b1838" stroke-width="1.6" fill="none"/></svg>3 MONTHS FREE SERVICE.</li>
      <li><svg width="13" height="13" viewBox="0 0 13 13"><circle cx="6.5" cy="6.5" r="6.5" fill="#fff200"/><path d="M3.6 6.7l2 2 3.8-4" stroke="#0b1838" stroke-width="1.6" fill="none"/></svg>1 YEAR CONTRACT.</li>
      <li><svg width="13" height="13" viewBox="0 0 13 13"><circle cx="6.5" cy="6.5" r="6.5" fill="#fff200"/><path d="M3.6 6.7l2 2 3.8-4" stroke="#0b1838" stroke-width="1.6" fill="none"/></svg>HIPAA COMPLIANT.</li>
      <li><svg width="13" height="13" viewBox="0 0 13 13"><circle cx="6.5" cy="6.5" r="6.5" fill="#fff200"/><path d="M3.6 6.7l2 2 3.8-4" stroke="#0b1838" stroke-width="1.6" fill="none"/></svg>LOCAL SERVICE AND SUPPORT.</li>
    </ul>

    <div class="feature feature--features">
      <div class="feature__icon"><svg width="42" height="38" viewBox="0 0 42 38" fill="none" stroke="#fff" stroke-width="1.6"><rect x="2" y="2" width="38" height="26" rx="2"/><rect x="6" y="6" width="30" height="18"/><path d="M21 28v6M14 35h14"/><path d="M10 21v-4M15 21v-6M20 21v-3M25 21v-7M30 21v-9"/><path d="M9 15l6-4 5 3 6-5 6 1"/></svg></div>
      POWERFUL<br>FEATHURES
    </div>
    <div class="feature feature--ease">
      <div class="feature__icon"><svg width="42" height="40" viewBox="0 0 42 40" fill="none" stroke="#fff" stroke-width="1.6"><rect x="3" y="3" width="36" height="28" rx="2"/><path d="M3 10h36"/><circle cx="8" cy="6.5" r="1.2"/><circle cx="12" cy="6.5" r="1.2"/><circle cx="16" cy="6.5" r="1.2"/><path d="M9 15h24M9 19h18M9 23h24"/><path d="M26 25l3 11 2-4 4 4 2-2-4-4 4-2z" fill="#0a4f9a"/></svg></div>
      ESAY TO USE
    </div>
    <div class="feature feature--setup">
      <div class="feature__icon"><svg width="40" height="40" viewBox="0 0 40 40" fill="none" stroke="#fff" stroke-width="1.6"><path d="M10 4h4v10l-1 2v16a1 1 0 0 1-2 0V16l-1-2z"/><rect x="9" y="28" width="6" height="9" rx="2"/><path d="M24 6a6 6 0 0 0 2 10v18a2 2 0 0 0 4 0V16a6 6 0 0 0 2-10v6h-8z"/></svg></div>
      EASY SET UP
    </div>
  </section>

  <footer class="footer">
    <div class="brand-bottom">Qorvane</div>
    <p class="cta">CALL TODAY FOR YOUR <b>FREE PHONE</b></p>
    <div class="phone-pill">
      <svg width="22" height="22" viewBox="0 0 24 24" fill="#fff"><path d="M6.6 10.8a15 15 0 0 0 6.6 6.6l2.2-2.2a1 1 0 0 1 1-.25 11.4 11.4 0 0 0 3.6.57 1 1 0 0 1 1 1V20a1 1 0 0 1-1 1A17 17 0 0 1 3 4a1 1 0 0 1 1-1h3.5a1 1 0 0 1 1 1c0 1.250.2 2.45.57 3.57a1 1 0 0 1-.25 1z"/></svg>
      555-018-2746
    </div>
    <p class="web">WWW.QORVANEVOICE.COM</p>
    <ul class="socials">
      <li>Loopit</li><li>Chatterly</li><li>Flitter</li><li>Snapgram</li><li>Tunely</li>
    </ul>
  </footer>
</main>
</body>
</html>
```